Website Online Research Solutions

We are a small European high-tech online research company.
With our own state of the art software we run online panels and are conducting reseach for companies. Partly research via our own panel and partly via panels we maintain for our customers.
Our current website is old and outdatet: www.pravelo.nl.
We are in the process to change the content of the site. We want a modern, european and businesslike design for our new website.
Our logo has to stay the same (left uppersite of our website and attached) but can be changed a little to adapt it to the new design of the website. The colors of the site are up to you.
Target Market(s)
Marketeers and researchers of large and middle size companies in all kind of fields.
Industry/Entity Type
Online
Look and feel
Each slider illustrates characteristics of the customer's brand and the style your logo design should communicate.

```html
<!DOCTYPE html>
<html lang="nl">
<head>
<meta charset="utf-8">
<title>Pravelo – Online Research Solutions</title>
<link href="https://fonts.googleapis.com/css2?family=Arimo:wght@400;700&display=swap" rel="stylesheet">
<style>
:root{
  --hero-top:#0d4a8c;
  --hero-bottom:#1c5aa6;
  --band:#17264d;
  --ink:#111;
  --heading:#143a6e;
  --lead:#555c66;
  --link:#2a3f8a;
  --panel-a:#1c6fae;
  --panel-b:#3aa0d0;
  --panel-edge:#123f6a;
  --footer:#6d6d6d;
  --footer-text:#c9c9c9;
  --white:#fff;
  --accent:#4fb0ff;
}
*{box-sizing:border-box;margin:0;padding:0}
html,body{width:1200px;height:1050px;overflow:hidden}
body{font-family:"Arimo",Arial,sans-serif;background:#fff;position:relative;color:var(--ink)}
.abs{position:absolute}
.hero{left:0;top:0;width:1200px;height:409px;background:radial-gradient(ellipse at 70% 60%,#2563b0 0%,var(--hero-bottom) 35%,var(--hero-top) 100%)}
.utility{top:23px;left:935px;font-size:11px;color:#dfe8f5;display:flex;gap:12px}
.utility span.sep{opacity:.7}
.brand{left:135px;top:40px;width:190px;height:150px;display:flex;align-items:center;gap:10px}
.brand-circle{width:150px;height:150px;border-radius:50%;background:linear-gradient(#d9d9d9,#8c8c8c);display:flex;align-items:center;justify-content:center}
.brand-name{font-size:26px;font-weight:700;color:#2d2d2d;letter-spacing:1px}
.nav{top:97px;left:0;width:1200px;height:24px}
.nav a{position:absolute;top:0;line-height:24px;font-size:13.5px;font-weight:700;color:var(--white);text-decoration:none}
.nav a.active{background:#0f3366;border-radius:12px;padding:0 29px;margin-left:-29px}
.hero-title{left:196px;top:238px;font-size:29px;font-weight:700;color:var(--white)}
.hero-text{left:196px;top:277px;font-size:17px;line-height:29px;color:#e6eefa;width:420px}
.hero-art{left:618px;top:124px;width:410px;height:294px;border-radius:50%;background:radial-gradient(ellipse at 45% 40%,rgba(180,200,230,.55),rgba(40,90,160,.15) 70%,transparent 75%)}
.band{left:0;top:409px;width:1200px;height:69px;background:var(--band)}
.sub{top:424px;display:flex;gap:9px;align-items:flex-start}
.sub svg{flex:none;margin-top:3px}
.sub p{font-size:16px;font-weight:700;color:var(--white);line-height:19px}
.sub p b{color:var(--accent)}
.main-title{left:166px;top:496px;font-size:21px;font-weight:700;color:var(--heading)}
.lead{left:166px;top:526px;width:500px;font-size:12.5px;font-weight:700;line-height:17.5px;color:var(--lead)}
.body{left:166px;width:500px;font-size:11px;line-height:17px;color:var(--ink)}
.photo{left:165px;top:689px;width:328px;height:228px;border:1px solid #ccc;background:linear-gradient(#fff,#e4eef4)}
.panel{left:720px;top:494px;width:315px;height:420px;border-radius:10px;border:2px solid var(--panel-edge);background:linear-gradient(135deg,var(--panel-a),var(--panel-b) 60%,var(--panel-a))}
.panel h2{position:absolute;left:11px;top:10px;font-size:21px;font-weight:700;color:var(--white)}
.video{position:absolute;left:10px;top:38px;width:228px;height:192px;background:#2b2b2b;padding:7px}
.video .screen{width:100%;height:160px;background:linear-gradient(#f6f6f6,#dcdcdc);border-radius:4px}
.video .bar{margin-top:6px;height:8px;border-radius:4px;background:#555}
.panel p{position:absolute;left:10px;top:244px;width:300px;font-size:10.6px;line-height:15.2px;color:var(--white)}
.footer{left:0;top:932px;width:1200px;height:118px;background:var(--footer)}
.fcol{top:15px;font-size:10.5px;line-height:13.5px;color:var(--footer-text)}
.fcol strong{color:#dedede}
.fmark{left:624px;top:30px;width:68px;height:68px;border-radius:50%;background:linear-gradient(#cfcfcf,#8a8a8a)}
.social{top:17px;left:764px;display:flex;gap:10px}
.social span{width:21px;height:21px;border-radius:3px;background:#3d6ea8}
</style>
</head>
<body>
<header class="abs hero">
  <div class="abs utility"><span>Home</span><span class="sep">|</span><span>Site Map</span></div>
  <div class="abs brand"><div class="brand-circle"><span class="brand-name">PRAVELO</span></div></div>
  <nav class="abs nav">
    <a style="left:378px">Algemeen</a>
    <a class="active" style="left:490px">Producten</a>
    <a style="left:597px">Demo’s</a>
    <a style="left:699px">Media</a>
    <a style="left:781px">Referenties</a>
    <a style="left:880px">Peresoneel</a>
    <a style="left:987px">Contact</a>
  </nav>
  <div class="abs hero-art" role="img" aria-label="Magnifying glass over the word search repeated in many type styles"></div>
  <h1 class="abs hero-title">Online Research Solutions</h1>
  <p class="abs hero-text">Aliquipit nis nis ad eriuscil utem vent prationsed el digna alit nonulluptat, venibh exerostie magnaeril ius.</p>
</header>

<section class="abs band">
  <div class="abs sub" style="left:176px;top:15px">
    <svg width="30" height="30" viewBox="0 0 30 30"><circle cx="15" cy="15" r="14" fill="#2b74d0"/><text x="15" y="21" text-anchor="middle" font-family="Arimo,sans-serif" font-size="18" font-weight="700" fill="#fff">?</text></svg>
    <p>Sub Headline<br>One <b>&gt;&gt;</b></p>
  </div>
  <div class="abs sub" style="left:375px;top:15px">
    <svg width="30" height="30" viewBox="0 0 30 30"><circle cx="15" cy="15" r="14" fill="#2b74d0"/><text x="15" y="21" text-anchor="middle" font-family="Arimo,sans-serif" font-size="18" font-weight="700" fill="#fff">?</text></svg>
    <p>Sub Headline<br>Two <b>&gt;&gt;</b></p>
  </div>
  <div class="abs sub" style="left:566px;top:15px">
    <svg width="30" height="30" viewBox="0 0 30 30"><circle cx="15" cy="15" r="14" fill="#2b74d0"/><text x="15" y="21" text-anchor="middle" font-family="Arimo,sans-serif" font-size="18" font-weight="700" fill="#fff">?</text></svg>
    <p>Sub Headline<br>Three <b>&gt;&gt;</b></p>
  </div>
  <div class="abs sub" style="left:788px;top:15px">
    <svg width="30" height="30" viewBox="0 0 30 30"><circle cx="15" cy="15" r="14" fill="#2b74d0"/><text x="15" y="21" text-anchor="middle" font-family="Arimo,sans-serif" font-size="18" font-weight="700" fill="#fff">?</text></svg>
    <p>Sub Headline<br>Four <b>&gt;&gt;</b></p>
  </div>
</section>

<main>
  <h2 class="abs main-title">Dataverzameling</h2>
  <p class="abs lead">Vragenlijsten die door Pravelo worden geprogrammeerd zijn dynamisch gegenereerde vragenlijsten die in de "look &amp; feel" worden geprogrammeerd van onze klanten en/of de produkten van onze klanten.</p>
  <p class="abs body" style="top:585px">Pravelo programmeert vragenlijsten/enquetes voor gegevensverzameling via internet, intranet of via email. Recentelijk hebben we zelfs betrouwbare methoden ontwikkeld voor onderzoek via SMS.</p>
  <p class="abs body" style="top:626px">De vele honderden onderzoeken die wij hebben geprogrammeerd varieren van eenvoudige onderzoeken via quickpolls met een aantal korte stellingen of banners tot en met complexe (inter)nationale multilinguale monitoren, medewerker&amp;klanttevredenheid onderzoek, usability tests etc.</p>
  <div class="abs photo" role="img" aria-label="Network of blue figures with one red figure under a magnifying glass"></div>

  <aside class="abs panel">
    <h2>Streaming audio/video</h2>
    <div class="video">
      <div class="screen" role="img" aria-label="Hand drawing a marketing diagram on a whiteboard"></div>
      <div class="bar"></div>
    </div>
    <p>Daarnaast hebben we betrouwbare en eenvoudige technieken ontwikkeld voor online onderzoek ten behoeve van pre-testing van radio&amp;TV commercials waarbij gebruik gemaakt wordt van streaming audio/video. Pravelo stelt haar opdrachtgevers vervolgens in staat om op eenvoudige wijze de verzamelde onderzoeksgegevens online te bekijken en deze eveneens online te analyseren via een online analysetool. Doordat deze analyse- tool zeer gebruikers-vriendelijk werd ontworpen is deze niet alleen geschikt voor opinieonder- zoekbureau’s maar ook voor bedrijven met een eigen researchafdeling en/of ervaren opinieonderzoekers.</p>
  </aside>
</main>

<footer class="abs footer">
  <div class="abs fcol" style="left:210px"><strong>The Service</strong><br>About<br>Browse<br>Log In</div>
  <div class="abs fcol" style="left:334px"><strong>Support</strong><br>Contact Us<br>FAQ</div>
  <div class="abs fcol" style="left:451px"><strong>Legal</strong><br>Privacy Policy<br>Terms &amp; Conditions</div>
  <div class="abs fcol" style="left:624px"><strong>© 2010 Pravelo</strong></div>
  <div class="abs fmark"></div>
  <div class="abs social"><span></span><span></span><span></span><span style="background:#d9772c"></span></div>
</footer>
</body>
</html>
```